Course flyer - evolutive design

We want to have a nice design for our course programm.
In fact we are school language, and our course programm change approximatively each 2 weeks§.
For that we need a design that we can modify each 2 weeks (only dates change ) by ourselves.
We used to have a classical design but we want to upgrade it with a modern and attractive design.
We can have 3 versions one for each city.
We have 3 offices: Tunis, Sousse & Marsena
Attached you can find old designs

Target Market(s)

students from 16 years old till retired people 76 years old

Industry/Entity Type

Education

Font styles to use
Sans Serif

Requirements
Must have
• clear timing for courses (date, days, timing)
• prices
• Adresse (each flyer has its own adress)
• phone Number
• Cool image
Should not have
• Racism
• Violence
• Too much stuff

```html
<!DOCTYPE html>
<html lang="fr">
<head>
<meta charset="utf-8">
<title>Cours d'allemand – Mai Juin – Marsena</title>
<link rel="stylesheet" href="https://fonts.googleapis.com/css2?family=Oswald:wght@600;700&family=PT+Sans:wght@400;700&family=Tinos:wght@700&display=swap">
<style>
  :root {
    --lime: #d6df22;
    --lime-bright: #e2e617;
    --ink: #111111;
    --white: #ffffff;
    --social: #3b5998;
    --photo-top: #6f8a3c;
    --photo-mid: #9aa3ad;
    --photo-low: #2d4f86;
    --photo-skin: #d9b8a3;
  }
  * { margin: 0; padding: 0; box-sizing: border-box; }
  html, body { width: 681px; height: 1200px; overflow: hidden; background: #ffffff; }
  .flyer {
    position: relative; width: 681px; height: 1200px; overflow: hidden;
    font-family: "PT Sans", Verdana, sans-serif; color: var(--ink);
  }
  .hero-photo {
    position: absolute; inset: 0;
    background:
      radial-gradient(ellipse 260px 220px at 360px 330px, var(--photo-skin), rgba(217,184,163,0) 70%),
      radial-gradient(ellipse 300px 260px at 480px 80px, #5a3a2a, rgba(90,58,42,0) 70%),
      linear-gradient(180deg, var(--photo-top) 0%, #8b9a70 28%, var(--photo-mid) 55%, var(--photo-low) 80%, #1e3a6a 100%);
  }
  .decor { position: absolute; inset: 0; }
  .abs { position: absolute; white-space: nowrap; }

  .brand { left: 34px; top: 96px; display: flex; align-items: center; gap: 12px; }
  .brand-dot { width: 30px; height: 30px; border-radius: 50%; background: var(--lime); }
  .brand-name { font-family: "Oswald", sans-serif; font-weight: 700; font-size: 58px; line-height: 1; color: var(--ink); letter-spacing: -1px; }

  .title { left: 445px; top: 32px; font-family: "Oswald", sans-serif; font-weight: 700; font-size: 37px; line-height: 44px; color: var(--lime-bright); letter-spacing: 0.5px; }
  .period { left: 460px; top: 133px; font-size: 27px; color: var(--white); }

  .course-name { font-family: "Oswald", sans-serif; font-weight: 700; font-size: 44px; line-height: 1; color: var(--ink); transform: translateY(-50%); letter-spacing: -0.5px; }
  .course-line { font-weight: 700; font-size: 20px; letter-spacing: 0.3px; line-height: 1; transform: translateY(-50%); }

  .contact-email { left: 407px; top: 946px; transform: translateY(-50%); font-family: "Tinos", serif; font-weight: 700; font-size: 22px; color: var(--ink); }
  .social-square { left: 453px; top: 848px; width: 50px; height: 50px; background: var(--social); }

  .office-city { left: 51px; top: 1035px; transform: translateY(-50%); font-family: "Oswald", sans-serif; font-weight: 700; font-size: 28px; color: var(--ink); }
  .office-address { left: 51px; top: 1052px; font-size: 17.5px; line-height: 21.5px; color: var(--white); font-style: normal; }

  .notes { left: 330px; top: 1026px; list-style: none; font-family: "Tinos", serif; font-weight: 700; font-size: 15px; line-height: 19px; color: var(--ink); }
  .notes li { position: relative; padding-left: 17px; margin-bottom: 8px; }
  .notes li::before { content: ""; position: absolute; left: 0; top: 5px; width: 8px; height: 8px; background: var(--ink); }
</style>
</head>
<body>
<main class="flyer">
  <div class="hero-photo" role="img" aria-label="Photo d'une jeune étudiante souriante, allongée dans l'herbe avec un cahier ouvert"></div>

  <svg class="decor" width="681" height="1200" viewBox="0 0 681 1200" aria-hidden="true">
    <circle cx="470" cy="380" r="250" fill="none" stroke="var(--lime)" stroke-width="48" stroke-opacity="0.55"/>
    <circle cx="470" cy="380" r="175" fill="none" stroke="var(--lime)" stroke-width="30" stroke-opacity="0.45"/>
    <circle cx="500" cy="600" r="300" fill="none" stroke="var(--lime)" stroke-width="22" stroke-opacity="0.35"/>
    <circle cx="167" cy="456" r="178" fill="var(--lime)"/>
    <circle cx="506" cy="606" r="172" fill="var(--lime)"/>
    <circle cx="206" cy="840" r="178" fill="var(--lime)"/>
  </svg>

  <div class="abs brand"><span class="brand-name">lingora group</span><span class="brand-dot"></span></div>

  <h1 class="abs title">COURS<br>D’ALLEMAND</h1>
  <p class="abs period">Mai Juin</p>

  <section class="course-intensif">
    <h2 class="abs course-name" style="left:67px;top:374px">Intensif</h2>
    <p class="abs course-line" style="left:67px;top:425px">Du 30 Mai au 17 Juin 2016</p>
    <p class="abs course-line" style="left:119px;top:465px">DuLundi Au Vendredi</p>
    <p class="abs course-line" style="left:39px;top:506px">8:30 à 11:00 &amp; 11:30 à 14:30</p>
    <p class="abs course-line" style="left:245px;top:545px">390 dt.</p>
  </section>

  <section class="course-super-intensif">
    <h2 class="abs course-name" style="left:387px;top:536px">Super Intensif</h2>
    <p class="abs course-line" style="left:386px;top:584px">Du 30 Mai au 10 Juin 2016</p>
    <p class="abs course-line" style="left:440px;top:626px">DuLundi Au Vendredi</p>
    <p class="abs course-line" style="left:360px;top:668px">9:00 à 13:30 &amp; 13:30 à 18:00</p>
    <p class="abs course-line" style="left:565px;top:707px">390 dt.</p>
  </section>

  <section class="course-extensif">
    <h2 class="abs course-name" style="left:85px;top:738px">Extensif</h2>
    <p class="abs course-line" style="left:85px;top:788px">Du 30 Mai au 13 Juillet 2016</p>
    <p class="abs course-line" style="left:95px;top:829px">Lundi, Mercredi &amp; Vendredi</p>
    <p class="abs course-line" style="left:207px;top:869px">15:00 à &nbsp;16:30</p>
    <p class="abs course-line" style="left:283px;top:907px">390 dt.</p>
    <p class="abs course-line" style="left:75px;top:944px">Première inscription: 15 dt.</p>
  </section>

  <div class="abs social-square"></div>
  <p class="abs contact-email">education@lingora.org</p>

  <section class="office">
    <h3 class="abs office-city">Marsena</h3>
    <address class="abs office-address">
      Imm. Yasmine, 5th floor of Palm Av.<br>
      Rue des Oliviers<br>
      (next to the central library)<br>
      4180, Marsena<br>
      Tel .: 74 512 600<br>
      E-mail: marsena [@] lingora.org
    </address>
  </section>

  <ul class="abs notes">
    <li>Toutes les inscription<br>dolvent imperative ment se faire au plus tard<br>une semaine avant le debut de cours</li>
    <li>Nombre minimum de 5<br>participants requis</li>
    <li>L’horaire de cours est susceptible<br>d’etre modifie</li>
  </ul>
</main>
</body>
</html>
```